Web site for small printshop

I am looking for a website for small printshop in Iceland, mainly serving university students and artist.

We print posters, flyers, business cards and more.

In addition to our current website, I would like to include design tool, (fx. www.quarvelink.com, www.tandorizo.com or something similar) jobs upload, shopping chart.
Updates

Great work, I am really amazed of the quality of work i am seeing here.

Really way beyond my expectation

GOOD JOB - all of you ! 

Hi all.

The designs submitted have been great, way better than expected.
I really did not expect this level of quality.

Some have been asking me for feedback on their designs, and I will try 
to send some feedback here, without spoiling your creativity.

Likes:
- when the colors of my logo is used in menus, buttons etc.
- simple, not to crowded look.

Dislikes.
- Dark and heavy design
- Lot of text and buttons (crowded look)

Extra info.
- top line (before menus) will contain: Tel - email - language
- menu line will have 5 categories: Home - service - submission of works - FAQ - about us
- 3 large buttons:  Job submit - Job design - ask for offer

LOVE YOUR WORK - great designs so far :)

Target Market(s)

University Students, Artists. Age group 20-30

Industry/Entity Type

University

Requirements
Must have
• The website must be easy to use, clean looking.

```html
<!DOCTYPE html>
<html lang="en">
<head>
<meta charset="utf-8">
<title>Kvarsi Studio – Print Media</title>
<link href="https://fonts.googleapis.com/css2?family=Poppins:wght@500&family=Open+Sans:wght@400;600&family=Roboto+Condensed:wght@400&family=Arimo:wght@400&display=swap" rel="stylesheet">
<style>
  :root {
    --ink-dark: #231f20;
    --brand-yellow: #fdd400;
    --brand-red: #e8312e;
    --page-grey: #e1e1e1;
    --tile-grey: #e8e8e8;
    --button-grey: #a9a9a9;
    --text-grey: #6a6a6a;
    --text-dark: #3f3f3f;
    --white: #ffffff;
  }
  * { margin: 0; padding: 0; box-sizing: border-box; }
  html, body { width: 1200px; height: 1000px; overflow: hidden; }
  body {
    position: relative;
    background: var(--page-grey);
    font-family: "Open Sans", sans-serif;
    color: var(--text-dark);
  }
  .topbar {
    position: absolute; left: 0; top: 0; width: 1200px; height: 21px;
    background: var(--ink-dark); color: #e6e6e6;
    font-family: "Arimo", sans-serif; font-size: 11px; line-height: 25px;
  }
  .topbar .email { position: absolute; left: 205px; }
  .topbar .contact { position: absolute; right: 136px; }
  .topbar .contact .divider { margin: 0 10px; }
  .site-header {
    position: absolute; left: 0; top: 21px; width: 1200px; height: 114px;
    background: var(--white);
  }
  .brand {
    position: absolute; left: 203px; top: 30px; height: 60px;
    display: flex; align-items: center; gap: 16px;
  }
  .brand-dot { width: 34px; height: 34px; border-radius: 50%; background: var(--brand-yellow); }
  .brand-name {
    font-family: "Open Sans", sans-serif; font-weight: 400; font-size: 34px;
    color: var(--text-dark);
  }
  .main-nav {
    position: absolute; left: 0; top: 135px; width: 1200px; height: 60px;
    background: var(--brand-yellow); border-bottom: 1px solid #e8c300;
  }
  .main-nav a {
    position: absolute; top: 0; line-height: 64px;
    font-family: "Poppins", sans-serif; font-weight: 500; font-size: 13.5px;
    color: var(--ink-dark); text-decoration: none; text-transform: uppercase;
  }
  .main-nav .sep { position: absolute; top: 22px; width: 1px; height: 26px; background: #f3e07a; }
  .hero {
    position: absolute; left: 202px; top: 222px; width: 998px; height: 233px;
    background: linear-gradient(to bottom, #fcfcfc, #efefef);
  }
  .hero-art {
    position: absolute; left: 0; top: 0; width: 400px; height: 233px;
    background: linear-gradient(135deg, #f4f4f4 0%, #e4e4e4 100%);
  }
  .tile { position: absolute; width: 83px; height: 83px; background: var(--tile-grey); border: 1px solid #d6d6d6; }
  .tile.light { background: #f6f6f6; }
  .hero-copy { position: absolute; right: 143px; top: 280px; text-align: right; }
  .hero-title { font-size: 40px; font-weight: 400; line-height: 48px; color: #444; letter-spacing: -1px; }
  .hero-title .accent { color: var(--brand-red); }
  .hero-rule { display: block; margin: 0 0 0 auto; width: 10px; height: 2px; background: var(--brand-red); }
  .hero-tagline { font-size: 17.5px; line-height: 26px; margin-top: 4px; color: #333; letter-spacing: -0.2px; }
  .hero-services { font-size: 14px; line-height: 24px; margin-top: 3px; color: #333; letter-spacing: -0.3px; }
  .action {
    position: absolute; top: 527px; width: 285px; height: 61px;
    background: var(--button-grey);
    font-family: "Roboto Condensed", sans-serif; font-size: 21px; color: var(--white);
  }
  .action.first { background: #f4f4f4; color: #8a8a8a; }
  .action .icon { position: absolute; left: 24px; top: 11px; width: 40px; height: 40px; border-radius: 6px; }
  .action .label { position: absolute; top: 17px; }
  .divider-line { position: absolute; left: 203px; top: 603px; width: 863px; height: 1px; background: #cdcdcd; }
  .tabs { position: absolute; left: 203px; top: 639px; display: flex; }
  .tab {
    width: 138px; height: 50px; line-height: 54px; text-align: center;
    font-family: "Arimo", sans-serif; font-size: 13px; color: #666;
    background: #ebebeb; border: 1px solid #d4d4d4; border-left: none;
  }
  .tab.active { width: 131px; background: var(--white); border-left: 1px solid #d4d4d4; border-bottom-color: var(--white); border-radius: 8px 0 0 0; }
  .panel {
    position: absolute; left: 203px; top: 688px; width: 863px; height: 230px;
    background: var(--white); border: 1px solid #d4d4d4; border-top: none; border-radius: 0 0 9px 9px;
  }
  .panel-heading { position: absolute; left: 25px; top: 17px; font-size: 17px; font-weight: 400; color: #666; }
  .panel-photo {
    position: absolute; left: 25px; top: 52px; width: 186px; height: 139px;
    background: linear-gradient(135deg, #2a2a2a 0%, #3a6a4c 45%, #111 100%);
  }
  .panel-text {
    position: absolute; left: 235px; top: 51px; width: 585px;
    font-family: "Arimo", sans-serif; font-size: 11px; line-height: 13.3px; color: var(--text-grey);
  }
  .panel-text p { margin-bottom: 13px; }
  .panel-text .more { color: #222; margin-top: 2px; }
  .site-footer {
    position: absolute; left: 0; top: 962px; width: 1200px; height: 38px;
    background: var(--ink-dark); color: #8d8d8d;
    font-family: "Arimo", sans-serif; font-size: 10px; line-height: 45px;
  }
  .site-footer .copyright { position: absolute; left: 206px; }
</style>
</head>
<body>
  <div class="topbar">
    <span class="email">Email: info@example.com</span>
    <span class="contact">Call: 123 4567 89000<span class="divider">|</span>ENGLISH | AU | FR</span>
  </div>

  <header class="site-header">
    <div class="brand">
      <span class="brand-dot"></span>
      <span class="brand-name">Kvarsi Studio</span>
    </div>
  </header>

  <nav class="main-nav">
    <a style="left:204px">Home</a>
    <span class="sep" style="left:266px"></span>
    <a style="left:298px">Services</a>
    <span class="sep" style="left:380px"></span>
    <a style="left:403px">Submitions of Work</a>
    <span class="sep" style="left:566px"></span>
    <a style="left:589px">FAQ</a>
    <span class="sep" style="left:643px"></span>
    <a style="left:666px">About Us</a>
  </nav>

  <section class="hero">
    <div class="hero-art" role="img" aria-label="Paint buckets pouring cyan, magenta, yellow and black paint onto large CMYK letters"></div>
  </section>
  <div class="tile" style="left:684px;top:331px"></div>
  <div class="tile" style="left:603px;top:413px"></div>
  <div class="tile" style="left:765px;top:413px"></div>
  <div class="tile light" style="left:847px;top:413px"></div>

  <div class="hero-copy">
    <h1 class="hero-title"><span class="accent">Print</span> Media</h1>
    <span class="hero-rule"></span>
    <p class="hero-tagline">Touch the Future</p>
    <p class="hero-services">Broucher, Flyer &amp; Business Card Design</p>
  </div>

  <a class="action first" style="left:203px">
    <span class="icon" role="img" aria-label="Upload icon" style="background:#2a8a63;border-radius:50%"></span>
    <span class="label" style="left:97px">Job Submit</span>
  </a>
  <a class="action" style="left:492px">
    <span class="icon" role="img" aria-label="Design tools icon" style="background:#d9a24a"></span>
    <span class="label" style="left:123px">Job Design</span>
  </a>
  <a class="action" style="left:781px">
    <span class="icon" role="img" aria-label="Offer request icon" style="background:#3b6aa8"></span>
    <span class="label" style="left:107px">Ask For Offer</span>
  </a>

  <div class="divider-line"></div>

  <div class="tabs">
    <div class="tab active">Business Card</div>
    <div class="tab">Print Posters</div>
    <div class="tab">Print Flyers</div>
  </div>

  <section class="panel">
    <h2 class="panel-heading">Heading</h2>
    <div class="panel-photo" role="img" aria-label="Photo of green and white printed business cards"></div>
    <div class="panel-text">
      <p>Lorem Ipsum is simply dummy text of the printing and typesetting industry. Lorem Ipsum has been the industry's stan-<br>dard dummy text ever since</p>
      <p>Lorem Ipsum is simply dummy text of the printing and typesetting industry. Lorem Ipsum has been the industry's stan-<br>dard dummy text ever sinceLorem Ipsum is simply dummy text of the printing and typesetting industry. Lorem Ipsum has<br>been the industry's standard dummy text ever since</p>
      <p>Lorem Ipsum is simply dummy text of the printing and typesetting industry. Lorem Ipsum has been the industry's stan-<br>dard dummy text ever since</p>
      <p class="more">+read more</p>
    </div>
  </section>

  <footer class="site-footer">
    <span class="copyright">2013.All Right Reserved</span>
  </footer>
</body>
</html>
```